Corvalen Coffee Bag for Retail Desing

.Our name and logo represent two things about the identity of our brand Turquoise Blue which is the color of the Honduras flag and the Guacamaya Bird (Ara Macao) national bird of Honduras we want that our logo and our packing reflects the peace that you can find by brewing your coffee and also the quality of our product which comes from one of the greatest coffee beans in the world.

We are looking for a design for our coffee bag there are some elements that we need to incorporate into the bag and we are providing you with a word document with guidelines to do it

Target Market(s)

Specialty coffee consumers is the United States

Industry/Entity Type

Product

Logo Text

CORVALEN COFFEE

Colors

Designer to choose colors to be used in the design.

Requirements
Must have
• Logo / Name of Brand
• Please Check Guidelines on Word Document
Nice to have
• The bag will be sent to print and all details are customizable feel free to be creative
Should not have

```html
<!DOCTYPE html>
<html lang="en">
<head>
<meta charset="utf-8">
<title>Corvalen Coffee – Retail Bag Designs</title>
<link href="https://fonts.googleapis.com/css2?family=Exo+2:wght@400;500&family=Open+Sans:wght@400;600&display=swap" rel="stylesheet">
<style>
  :root {
    --backdrop: #2f5f5c;
    --navy: #061a2b;
    --navy-deep: #04121f;
    --royal: #1e88e5;
    --sky: #3fa9f5;
    --cyan: #17d6e6;
    --cyan-light: #4ff0f5;
    --teal: #0a7f8f;
    --teal-dark: #0b4f5e;
    --white: #ffffff;
    --mist: #d8eef5;
  }
  html, body {
    margin: 0;
    padding: 0;
    width: 1200px;
    height: 774px;
    overflow: hidden;
    background: var(--backdrop);
  }
  .canvas {
    position: relative;
    width: 1200px;
    height: 774px;
  }
  .bag {
    position: absolute;
    width: 258px;
    height: 574px;
    box-shadow: 0 6px 18px rgba(0, 0, 0, 0.35);
  }
  .bag svg { display: block; width: 258px; height: 574px; }
  .bag--classic { left: 146px; top: 98px; }
  .bag--curve   { left: 470px; top: 94px; }
  .bag--facet   { left: 800px; top: 98px; }
  .title   { font-family: "Exo 2", sans-serif; font-weight: 500; }
  .origin  { font-family: "Exo 2", sans-serif; font-weight: 400; }
  .details { font-family: "Open Sans", sans-serif; font-weight: 400; }
  .weight  { font-family: "Open Sans", sans-serif; font-weight: 600; }
  .brand-name { font-family: "Exo 2", sans-serif; font-weight: 500; letter-spacing: 1px; }
</style>
</head>
<body>
<main class="canvas">

  <!-- Classic blue bag -->
  <section class="bag bag--classic" aria-label="Medium Dark coffee bag, classic blue">
    <svg viewBox="0 0 258 574">
      <defs>
        <linearGradient id="classic-bg" x1="0" y1="0" x2="1" y2="0.3">
          <stop offset="0" stop-color="var(--royal)"/>
          <stop offset="0.55" stop-color="#0d3a66"/>
          <stop offset="1" stop-color="var(--navy)"/>
        </linearGradient>
        <radialGradient id="classic-bird" cx="0.45" cy="0.4" r="0.7">
          <stop offset="0" stop-color="#1f6fb5"/>
          <stop offset="1" stop-color="#0b2c4e"/>
        </radialGradient>
      </defs>
      <rect class="bag-base" width="258" height="574" fill="url(#classic-bg)"/>
      <rect class="bag-illustration" role="img" aria-label="Large blue macaw illustration" x="0" y="214" width="258" height="352" fill="url(#classic-bird)" opacity="0.85"/>
      <path class="banner" d="M49 0 H210 V197 L129.5 219 L49 197 Z" fill="var(--navy)" stroke="var(--mist)" stroke-width="1"/>
      <circle class="brand-ring" cx="129.5" cy="138" r="56" fill="none" stroke="var(--sky)" stroke-width="1.5"/>
      <text class="brand-name" x="129.5" y="134" text-anchor="middle" font-size="13" fill="var(--sky)">CORVALEN</text>
      <text class="brand-name" x="129.5" y="151" text-anchor="middle" font-size="13" fill="var(--sky)">COFFEE</text>
      <text class="title" x="126" y="410" text-anchor="middle" font-size="22" fill="var(--sky)">Medium Dark</text>
      <text class="origin" x="126" y="432" text-anchor="middle" font-size="16" fill="var(--white)">100% Honduras</text>
      <text class="origin" x="126" y="448" text-anchor="middle" font-size="16" fill="var(--white)">Coffee</text>
      <text class="details" x="126" y="474" text-anchor="middle" font-size="10.5" fill="var(--mist)">Single Origin</text>
      <text class="details" x="126" y="489" text-anchor="middle" font-size="10.5" fill="var(--mist)">Small Batch Roasted</text>
      <text class="details" x="126" y="504" text-anchor="middle" font-size="10.5" fill="var(--mist)">Farm direct trade</text>
      <text class="weight" x="129" y="537" text-anchor="middle" font-size="9.5" fill="var(--white)">NET WT 16OZ</text>
      <text class="weight" x="129" y="551" text-anchor="middle" font-size="9.5" fill="var(--white)">(1LB 16OZ) 453g</text>
    </svg>
  </section>

  <!-- Cyan curve bag -->
  <section class="bag bag--curve" aria-label="Medium Dark coffee bag, cyan curve">
    <svg viewBox="0 0 258 574">
      <defs>
        <linearGradient id="curve-bg" x1="0" y1="0" x2="0" y2="1">
          <stop offset="0" stop-color="var(--teal)"/>
          <stop offset="1" stop-color="var(--teal-dark)"/>
        </linearGradient>
        <linearGradient id="curve-light" x1="0" y1="0" x2="1" y2="1">
          <stop offset="0" stop-color="var(--cyan-light)"/>
          <stop offset="1" stop-color="#0fb6c8"/>
        </linearGradient>
        <linearGradient id="curve-sketch" x1="0" y1="0" x2="0" y2="1">
          <stop offset="0" stop-color="#15324a"/>
          <stop offset="1" stop-color="var(--navy)"/>
        </linearGradient>
      </defs>
      <rect class="bag-base" width="258" height="574" fill="url(#curve-bg)"/>
      <path class="curve-sweep" d="M30 0 C 40 230, 150 420, 258 450 V0 Z" fill="url(#curve-light)"/>
      <rect class="bean-pattern" role="img" aria-label="Scattered coffee bean pattern" x="0" y="430" width="258" height="144" fill="var(--navy)"/>
      <path class="bean-fade" d="M0 380 C 80 420, 180 440, 258 440 V432 H0 Z" fill="var(--navy)" opacity="0.6"/>
      <path class="banner" d="M49 0 H209 V197 L129 219 L49 197 Z" fill="var(--navy)" stroke="var(--mist)" stroke-width="1"/>
      <rect class="branch-sketch" role="img" aria-label="Line sketch of a coffee branch with beans" x="74" y="38" width="110" height="84" fill="url(#curve-sketch)" opacity="0.7"/>
      <text class="title" x="129" y="153" text-anchor="middle" font-size="20" fill="var(--sky)">Medium Dark</text>
      <text class="origin" x="129" y="176" text-anchor="middle" font-size="14.5" fill="var(--white)">100% Honduras</text>
      <text class="origin" x="129" y="191" text-anchor="middle" font-size="14.5" fill="var(--white)">Coffee</text>
      <circle class="brand-disc" cx="130" cy="333" r="72" fill="var(--navy)"/>
      <circle class="brand-ring" cx="130" cy="333" r="66" fill="var(--white)"/>
      <text class="brand-name" x="130" y="329" text-anchor="middle" font-size="14" fill="var(--royal)">CORVALEN</text>
      <text class="brand-name" x="130" y="347" text-anchor="middle" font-size="14" fill="var(--royal)">COFFEE</text>
      <text class="details" x="129" y="472" text-anchor="middle" font-size="12.5" fill="var(--white)">Single Origin</text>
      <text class="details" x="129" y="489" text-anchor="middle" font-size="12.5" fill="var(--white)">Small Batch Roasted</text>
      <text class="details" x="129" y="506" text-anchor="middle" font-size="12.5" fill="var(--white)">Farm direct trade</text>
      <text class="weight" x="129" y="538" text-anchor="middle" font-size="9.5" fill="var(--white)">NET WT 16OZ</text>
      <text class="weight" x="129" y="552" text-anchor="middle" font-size="9.5" fill="var(--white)">(1LB 16OZ) 453g</text>
    </svg>
  </section>

  <!-- Faceted teal bag -->
  <section class="bag bag--facet" aria-label="Medium Dark coffee bag, faceted teal">
    <svg viewBox="0 0 258 574">
      <defs>
        <linearGradient id="facet-bg" x1="0" y1="0" x2="1" y2="1">
          <stop offset="0" stop-color="#0d6f7e"/>
          <stop offset="0.4" stop-color="var(--cyan)"/>
          <stop offset="0.7" stop-color="#10a9bb"/>
          <stop offset="1" stop-color="#0b5565"/>
        </linearGradient>
      </defs>
      <rect class="facet-pattern" role="img" aria-label="Geometric triangle mosaic in teal and cyan" width="258" height="574" fill="url(#facet-bg)"/>
      <circle class="brand-disc" cx="130" cy="156" r="73" fill="var(--navy)"/>
      <circle class="brand-ring" cx="130" cy="156" r="67" fill="var(--sky)"/>
      <text class="brand-name" x="130" y="152" text-anchor="middle" font-size="14" fill="var(--navy)">CORVALEN</text>
      <text class="brand-name" x="130" y="170" text-anchor="middle" font-size="14" fill="var(--navy)">COFFEE</text>
      <path class="label-diamond" d="M130 295 L226 382 L130 469 L34 382 Z" fill="rgba(255,255,255,0.18)" stroke="rgba(255,255,255,0.75)" stroke-width="1.5"/>
      <text class="origin" x="130" y="354" text-anchor="middle" font-size="16" fill="var(--navy)">Medium Dark</text>
      <text class="origin" x="130" y="375" text-anchor="middle" font-size="16" fill="var(--navy)">100% Honduras</text>
      <text class="origin" x="130" y="390" text-anchor="middle" font-size="16" fill="var(--navy)">Coffee</text>
      <text class="details" x="130" y="405" text-anchor="middle" font-size="9.5" fill="var(--navy)">Single Origin</text>
      <text class="details" x="130" y="415" text-anchor="middle" font-size="9.5" fill="var(--navy)">Small Batch Roasted</text>
      <text class="details" x="130" y="425" text-anchor="middle" font-size="9.5" fill="var(--navy)">Farm direct trade</text>
      <text class="weight" x="130" y="540" text-anchor="middle" font-size="9.5" fill="var(--white)">NET WT 16OZ</text>
      <text class="weight" x="130" y="554" text-anchor="middle" font-size="9.5" fill="var(--white)">(1LB 16OZ) 453g</text>
    </svg>
  </section>

</main>
</body>
</html>
```